New website

We ned to create a new website that reflects more who we are. We are delivering exclusive premium products to our customers and the current website does not reflect our products at all.
We believe in less is more and need a webpage that is clean yet professional and exclusive.

Target Market(s)

Dentistry

Industry/Entity Type

Dental

Number of Pages Required

5+ page

Font styles to use
Sans Serif

Colors

Designer to choose colors to be used in the design.

Requirements
Must have
• Picture gallery
• Nice structure
• Clean layout
Nice to have
• Light fonts
Should not have
• Any italic font styles

```html
<!DOCTYPE html>
<html lang="en">
<head>
<meta charset="utf-8">
<title>Novasmile – Dental Restorations</title>
<link href="https://fonts.googleapis.com/css2?family=Montserrat:wght@300;400;500;600;700&family=Lato:wght@300;400;700&display=swap" rel="stylesheet">
<style>
:root{
  --red:#e8304a;
  --red-dark:#c9223a;
  --blue:#1f72b8;
  --slate:#3b4a57;
  --ink:#2b2f36;
  --text:#444a52;
  --beige:#ece8e0;
  --paper:#ffffff;
  --footer:#2a2d34;
  --footer-dark:#202228;
  --muted:#9aa0a8;
}
*{box-sizing:border-box;margin:0;padding:0}
html,body{width:1200px;height:4712px;overflow:hidden}
body{font-family:"Lato",sans-serif;color:var(--text);background:var(--paper);position:relative}
h1,h2,h3,.brand,.nav a{font-family:"Montserrat",sans-serif}

/* Header */
.site-header{position:absolute;left:0;top:0;width:1200px;height:157px;background:var(--paper)}
.brand{position:absolute;left:52px;top:58px;font-size:28px;font-weight:500;letter-spacing:0;color:var(--ink)}
.phone-tab{position:absolute;left:940px;top:0;width:170px;height:42px;background:var(--red);color:#fff;font-size:15px;font-weight:700;display:flex;align-items:center;justify-content:center;gap:8px}
.nav{position:absolute;left:402px;top:66px;display:flex}
.nav a{display:block;padding:8px 16px;font-size:13px;font-weight:500;color:var(--ink);text-decoration:none;letter-spacing:.5px}
.nav a.active{background:var(--red);color:#fff}

/* Hero */
.hero{position:absolute;left:0;top:157px;width:1200px;height:803px}
.hero-photo{position:absolute;inset:0;background:linear-gradient(100deg,#6b5a52 0%,#8a6f5f 35%,#b8896e 55%,#5e5048 80%,#3e3a3c 100%)}
.hero-box{position:absolute;left:56px;top:235px;width:528px;height:440px;background:rgba(25,25,30,.82);border-left:6px solid var(--red);padding:60px 50px}
.hero-box h1{font-size:52px;font-weight:400;color:#fff;line-height:1.2}
.hero-box .amp{position:absolute;left:395px;top:20px;font-size:150px;font-weight:300;color:#fff;font-family:"Montserrat",sans-serif}
.hero-box p{margin-top:28px;font-size:15px;line-height:1.75;color:#e6e6e6}
.hero-dots{position:absolute;left:498px;top:660px;display:flex;gap:8px}
.hero-dots span{width:26px;height:26px;background:var(--red)}
.hero-dots span+span{background:var(--blue)}

/* Products */
.products{position:absolute;left:0;top:960px;width:1200px;height:1600px;background:var(--beige)}
.section-title{font-size:40px;font-weight:400;color:var(--ink);text-align:center}
.products .section-title{position:absolute;left:0;right:0;top:40px}
.product-grid{position:absolute;left:122px;top:123px;width:958px;display:grid;grid-template-columns:479px 479px;grid-auto-rows:337px}
.product-card{position:relative;padding:40px 54px 0 54px;color:#fff}
.product-card.red{background:var(--red)}
.product-card.blue{background:var(--blue)}
.product-card h3{font-size:32px;font-weight:600;margin-bottom:18px}
.product-card p{font-size:14px;line-height:1.75;color:rgba(255,255,255,.9)}
.read-more{position:absolute;right:14px;bottom:14px;background:var(--red-dark);color:#fff;font-size:12px;font-weight:700;padding:5px 12px}
.product-card.red .read-more{background:var(--blue)}
.call-card{background:var(--slate);color:#fff;text-align:center;padding-top:70px;font-family:"Montserrat",sans-serif}
.call-card .label{font-size:30px;font-weight:400;letter-spacing:2px}
.call-card .number{font-size:58px;font-weight:600;line-height:1.2;margin-top:10px}

/* Special services */
.tooth-badge{position:absolute;left:560px;top:2518px;width:80px;height:80px;border-radius:50%;background:var(--red);z-index:3;display:flex;align-items:center;justify-content:center}
.services{position:absolute;left:0;top:2560px;width:1200px;height:685px;background:linear-gradient(180deg,#cfcfd1 0%,#e2e1e3 50%,#c9c8cb 100%);border-top:5px solid var(--red)}
.services h2{position:absolute;left:184px;top:95px;font-size:40px;font-weight:400;color:var(--red)}
.services .copy{position:absolute;left:184px;top:200px;width:880px;font-size:15px;line-height:1.65;color:#2d2f33}
.services .copy p{margin-bottom:22px}

/* Call band */
.call-band{position:absolute;left:0;top:3245px;width:1200px;height:165px;background:var(--red);display:flex;align-items:center;justify-content:center;gap:38px}
.call-band .icon{width:100px;height:100px;border-radius:50%;background:#fff;display:flex;align-items:center;justify-content:center}
.call-band span{font-family:"Montserrat",sans-serif;font-size:52px;font-weight:400;color:#fff}

/* About */
.about{position:absolute;left:0;top:3410px;width:1200px;height:460px;background:var(--paper)}
.about h2{position:absolute;left:458px;top:30px;font-size:34px;font-weight:400;color:var(--ink)}
.about-photo{position:absolute;left:150px;top:140px;width:260px;height:185px;background:linear-gradient(160deg,#b9c2c8,#7f8b93 60%,#5c666d)}
.about .copy{position:absolute;left:458px;top:92px;width:630px;font-size:14px;line-height:1.7}
.about .copy p{margin-bottom:16px}
.about .read-more{position:static;display:inline-block;background:var(--blue)}

/* Testimonials */
.testimonials{position:absolute;left:0;top:3870px;width:1200px;height:420px;background:#eceae6}
.testimonials h2{position:absolute;left:0;right:0;top:80px;font-size:26px;font-weight:400;color:var(--blue);text-align:center}
.arrow-btn{position:absolute;top:231px;width:30px;height:30px;background:#555;display:flex;align-items:center;justify-content:center}
.quote{position:absolute;top:180px;width:400px;display:flex;gap:18px}
.quote .avatar{width:130px;height:130px;flex:none;background:linear-gradient(180deg,#c9c4be,#8d8780)}
.quote p{font-size:13px;line-height:1.55;color:#333}
.quote .name{margin-top:10px;font-weight:700;font-size:13px;color:var(--red)}

/* Footer */
.site-footer{position:absolute;left:0;top:4290px;width:1200px;height:360px;background:var(--footer);color:#d5d7da}
.site-footer .brand{left:74px;top:90px;color:#fff;font-size:26px}
.contact-list{position:absolute;left:100px;top:156px;font-size:13px;line-height:1.75;list-style:none}
.contact-list li::before{content:"";display:inline-block;width:7px;height:7px;background:var(--red);margin-right:8px}
.footer-col{position:absolute;top:92px}
.footer-col h3{font-size:15px;font-weight:600;color:#fff;margin-bottom:8px}
.footer-col ul{list-style:none;font-size:13px;line-height:1.5;color:var(--muted)}
.follow{position:absolute;left:602px;top:282px}
.follow h3{font-size:15px;font-weight:600;color:#fff;margin-bottom:10px}
.follow .dots{display:flex;gap:10px}
.follow .dots span{width:24px;height:24px;border-radius:50%;background:var(--red)}
.field{width:228px;height:32px;background:#fbf7df;margin-bottom:12px;font-size:12px;color:#888;padding:8px 10px}
.subscribe{display:flex;align-items:center;gap:8px;width:124px;height:34px;background:var(--red);color:#fff;font-size:14px;font-weight:700;padding-left:20px;margin-left:104px}
.footer-bar{position:absolute;left:0;top:4650px;width:1200px;height:62px;background:var(--footer-dark);font-size:12px;color:var(--muted)}
.footer-bar .copy{position:absolute;left:74px;top:22px}
.footer-bar .links{position:absolute;right:80px;top:22px;display:flex;gap:26px}
</style>
</head>
<body>

<header class="site-header">
  <div class="brand">Novasmile</div>
  <div class="phone-tab">
    <svg width="14" height="14" viewBox="0 0 24 24"><path fill="#fff" d="M6.6 10.8c1.4 2.8 3.8 5.1 6.6 6.6l2.2-2.2c.3-.3.7-.4 1-.2 1.1.4 2.3.6 3.6.6.6 0 1 .4 1 1V20c0 .6-.4 1-1 1C10.6 21 3 13.4 3 4c0-.6.4-1 1-1h3.5c.6 0 1 .4 1 1 0 1.3.2 2.5.6 3.6.1.3 0 .7-.2 1z"/></svg>
    +46-40-55 01 20
  </div>
  <nav class="nav">
    <a class="active">HOME</a><a>PRODUCTS</a><a>SPECIAL SERVICES</a><a>SMILE GALLERY</a><a>THE COMPANY</a><a>CONTACT US</a>
  </nav>
</header>

<section class="hero">
  <div class="hero-photo" role="img" aria-label="Smiling woman in sunglasses showing bright white teeth"></div>
  <div class="hero-box">
    <span class="amp">&amp;</span>
    <h1>Novasmile<br>Confidence</h1>
    <p>Premium dental restorations crafted with care, precision and modern materials. We help clinics give every patient a natural, lasting smile. Discover how our team, our lab and our products work together for results you can trust every day.</p>
  </div>
  <div class="hero-dots"><span></span><span></span></div>
</section>

<section class="products">
  <h2 class="section-title">Our Products</h2>
  <div class="product-grid">
    <article class="product-card red"><h3>Veneers</h3><p>For patients seeking to enhance the appearance of their smile or mask stained dentition, porcelain laminate veneers are the most indicated restorative method to date. To enhance the beauty and strength of the veneers we use standard shade porcelain systems. The high strength ceramic is fired on refractory dies and has the ability of masking stained dentition as well.</p><span class="read-more">Read More</span></article>
    <article class="product-card blue"><h3>Lumina Press</h3><p>We use different all ceramic systems to provide exceptional metal-free restorative results. Our initial approach addresses the aesthetic demands of a ceramic restoration with a shaded, translucent pressed core and ion fusing layering porcelains. The combination of these materials results in light-scattering properties that simulate natural dentition.</p><span class="read-more">Read More</span></article>
    <article class="product-card blue"><h3>Gradient Composite</h3><p>A restoration made from composite material has many beneficial properties such as strength and durability, but although composite also has good aesthetic qualities, it does not give the natural tooth appearance of a porcelain. That is, until now!</p><span class="read-more">Read More</span></article>
    <article class="product-card red"><h3>Arc Bridge</h3><p>The Arc bridge, a metal-free, dual-component system, eliminates the aesthetic and mechanical concerns of the conventional metal and bridge. Developed for single tooth replacement, this system incorporates the flexibility and strength of a polyaramid framework to provide the fiber reinforced composite bridge framework.</p><span class="read-more">Read More</span></article>
    <article class="product-card red"><h3>Pigments</h3><p>Novasmile's occlusal shade guide! Developed at Novasmile, the ultimate shade guide for occlusal characterizations. Now you don't have to guess how your technician is going to characterize the occlusal surface. With our pigments you can choose the characterization that you want, 15 different characterizations are available.</p><span class="read-more">Read More</span></article>
    <article class="product-card blue"><h3>Implants</h3><p>Implants are the perfect solution for patients that miss one or more teeth and will not accept a denture or a bridge. To make the implant constructions natural and life full, we work with a porcelain that is fluorescent, luminescent and opalescent. There is a lot of different implant systems to choose from and to say that one is better than the other is not our job.</p><span class="read-more">Read More</span></article>
    <article class="product-card blue"><h3>Zirconia</h3><p>Yttria stabilized zirconia is a material that has been used for highly exacting medical applications such as the fabrication of artificial hip ball joints for many years. The material has unique properties, for example it demonstrates high durability. The material does not lose these qualities, even when it is exposed to stresses, due to the crack-inhibiting properties of the microstructure.</p></article>
    <div class="call-card"><div class="label">CALL US</div><div class="number">+46-40-<br>55 01 20</div></div>
  </div>
</section>

<div class="tooth-badge">
  <svg width="38" height="42" viewBox="0 0 38 42"><path fill="#fff" d="M10 2c-6 0-9 5-8 12 1 6 3 10 4 18 1 6 5 10 7 5l3-9c1-3 4-3 5 0l3 9c2 5 6 1 7-5 1-8 3-12 4-18 1-7-2-12-8-12-4 0-6 2-9 2s-5-2-10-2z"/></svg>
</div>

<section class="services">
  <h2>Special Services</h2>
  <div class="copy">
    <p>Novasmile ensures exact teeth reconstruction, individual service of the customer and technical information. We can also offer our customers additional service on favorable terms. The below specified additional services are only a part of what we can offer to you and your patients.</p>
    <p>Novasmile Cosmetic Imaging is the first step in creating a blueprint for success. The patient can see the final result before taking any decisions. Click the links in the menu above to learn more!</p>
    <p>Novasmile Diagnostic Waxup is the first step in creating a blueprint template for success.<br>This will ensure patient acceptance and satisfaction.<br>You wouldn't start building a house without a blueprint, would you? Click the links in the menu above to learn more!</p>
    <p>Novasmile Color Test veneer is for the really demanding patient who wants nothing but perfection.<br>Click the links in the menu above to learn more!</p>
  </div>
</section>

<section class="call-band">
  <div class="icon"><svg width="50" height="50" viewBox="0 0 24 24"><path fill="#e8304a" d="M6.6 10.8c1.4 2.8 3.8 5.1 6.6 6.6l2.2-2.2c.3-.3.7-.4 1-.2 1.1.4 2.3.6 3.6.6.6 0 1 .4 1 1V20c0 .6-.4 1-1 1C10.6 21 3 13.4 3 4c0-.6.4-1 1-1h3.5c.6 0 1 .4 1 1 0 1.3.2 2.5.6 3.6.1.3 0 .7-.2 1z"/></svg></div>
  <span>Call Us:&nbsp; 1-800-555-0142</span>
</section>

<section class="about">
  <h2>About Novasmile</h2>
  <div class="about-photo" role="img" aria-label="Bright open dental laboratory with workstations"></div>
  <div class="copy">
    <p>Novasmile started at the beginning of 1998. Since then we provide our clients fixed restaurations of highest quality, mainly without metal frameworks.</p>
    <p>Our speciality is cosmetic/esthetic restaurations. Our goal is to produce high-quality products with the help of carefully selected products, equipment and of course the latest techniques. With this on our mind we can create a product with high quality, esthetic, fit and functionality. This is important when it comes to the cementation process, where you shouldn't waste valuable time to adjust or remake our work. With the patient in our mind you should always feel satisfied with our products.</p>
    <p>Novasmile follows the ISO 9000 qualityplan and the Swedish department of health standards concerning custom made medical devices.</p>
    <span class="read-more">Read More</span>
  </div>
</section>

<section class="testimonials">
  <h2>What our happy customers has to say</h2>
  <div class="arrow-btn" style="left:76px"><svg width="10" height="12" viewBox="0 0 10 12"><path fill="#fff" d="M8 0L0 6l8 6z"/></svg></div>
  <div class="quote" style="left:150px">
    <div class="avatar" role="img" aria-label="Portrait of a customer"></div>
    <div><p>"Working with this lab has been simple from day one. The results look natural and my patients are always pleased with their new smile."</p><div class="name">Erik Holm</div></div>
  </div>
  <div class="quote" style="left:654px">
    <div class="avatar" role="img" aria-label="Portrait of a customer"></div>
    <div><p>"Every case arrives on time and fits perfectly. Their team listens, advises and delivers work I am proud to place for my patients."</p><div class="name">Lina Berg</div></div>
  </div>
  <div class="arrow-btn" style="left:1090px"><svg width="10" height="12" viewBox="0 0 10 12"><path fill="#fff" d="M2 0l8 6-8 6z"/></svg></div>
</section>

<footer class="site-footer">
  <div class="brand">Novasmile</div>
  <ul class="contact-list">
    <li>Office: +46-40-55 01 20</li>
    <li>Email: hello@novasmile.example</li>
    <li>Mon - Fri : 7am - 6pm</li>
    <li>Sat : 8am - 2pm</li>
  </ul>
  <div class="footer-col" style="left:602px">
    <h3>Navigation</h3>
    <ul><li>Home</li><li>Products</li><li>Special Services</li><li>Smile Gallery</li><li>The Company</li><li>Shade Analysis</li><li>Contact Us</li></ul>
  </div>
  <div class="follow">
    <h3>Follow Us</h3>
    <div class="dots"><span></span><span></span><span></span><span></span></div>
  </div>
  <div class="footer-col" style="left:892px">
    <h3>Newsletter</h3>
    <div class="field">Name</div>
    <div class="field">Email</div>
    <div class="subscribe">Subscribe <svg width="8" height="10" viewBox="0 0 8 10"><path fill="#fff" d="M0 0l8 5-8 5z"/></svg></div>
  </div>
</footer>
<div class="footer-bar">
  <div class="copy">Copyright © 2017 Novasmile Dental Services AB</div>
  <div class="links"><span>Terms of Use</span><span>Privacy Policy</span><span>Directory</span></div>
</div>

</body>
</html>
```